Business Card Design

We are a church looking for marketing business card. Contact info Pastors name and a map on the back. Service times. Looking for something to grab attention. Not looking for personal card more of a generic card to pass out to new potential visitors.
Updates

Industry/Entity Type

Marketing

Contact Information for Business Card

Harbor Stone Fellowship Church
418 Willow Crest Pkwy suite 3-D Maplecrest GA 30299
(555)314-8862
Hsfcwebsite.org
Pastor Howard Pemberly
Sunday 12:00 pm
Wednesday prayer call 9:30 pm 5558807342 conference #8364152

```html
<!DOCTYPE html>
<html lang="en">
<head>
<meta charset="utf-8">
<title>Harbor Stone Fellowship Church – Business Cards</title>
<link rel="stylesheet" href="https://fonts.googleapis.com/css2?family=Arimo:wght@400;700&display=swap">
<style>
  :root {
    --bg: #e9e9ea;
    --card: #ffffff;
    --ink: #111111;
    --accent: #1fb6e8;
    --accent-soft: #bfe9f8;
    --edge: #b8322e;
  }
  html, body {
    margin: 0;
    padding: 0;
    width: 1200px;
    height: 843px;
    overflow: hidden;
    background: var(--bg);
    font-family: "Arimo", Arial, sans-serif;
    color: var(--ink);
  }
  .canvas {
    position: relative;
    width: 1200px;
    height: 843px;
  }
  .card {
    position: absolute;
    left: 280px;
    width: 640px;
    height: 366px;
    background: var(--card);
    border-bottom: 3px solid var(--edge);
    box-shadow: 0 6px 18px rgba(0,0,0,0.12);
    overflow: hidden;
  }
  .card--pastor { top: 37px; }
  .card--church { top: 437px; }
  .initial { color: var(--accent); }

  /* Pastor side */
  .rule-v {
    position: absolute;
    left: 340px;
    top: 88px;
    width: 2px;
    height: 218px;
    background: var(--accent);
  }
  .pastor-name {
    position: absolute;
    right: 312px;
    top: 146px;
    margin: 0;
    font-size: 34px;
    font-weight: 700;
    letter-spacing: -0.5px;
    white-space: nowrap;
  }
  .pastor-name .initial { font-size: 40px; }
  .pastor-title {
    position: absolute;
    right: 312px;
    top: 192px;
    margin: 0;
    font-size: 22px;
    font-weight: 700;
  }
  .service-times {
    position: absolute;
    left: 356px;
    top: 146px;
    margin: 0;
    font-size: 12px;
    font-weight: 700;
    line-height: 1.5;
    white-space: nowrap;
  }
  .service-times .conference { color: var(--accent); font-weight: 400; }

  /* Church side */
  .church-name {
    position: absolute;
    left: 42px;
    top: 40px;
    margin: 0;
    font-size: 25px;
    font-weight: 700;
    white-space: nowrap;
  }
  .church-contact {
    position: absolute;
    left: 42px;
    top: 82px;
    padding-left: 10px;
    border-left: 2px solid var(--accent);
    font-size: 14px;
    line-height: 1.5;
    white-space: nowrap;
  }
  .church-contact p { margin: 0; }
  .church-contact .web { color: var(--accent); }
  .church-illustration {
    position: absolute;
    right: 44px;
    bottom: 36px;
    width: 250px;
    height: 180px;
    background: linear-gradient(135deg, var(--accent-soft), var(--accent));
    opacity: 0.85;
  }
</style>
</head>
<body>
<main class="canvas">

  <section class="card card--pastor" aria-label="Pastor card">
    <div class="rule-v"></div>
    <h1 class="pastor-name"><span class="initial">H</span>oward <span class="initial">P</span>emberly</h1>
    <p class="pastor-title">pastor</p>
    <p class="service-times">
      Sunday 12:00 pm<br>
      Wednesday prayer call 9:30 pm 5558807342<br>
      <span class="conference">conference #8364152</span>
    </p>
  </section>

  <section class="card card--church" aria-label="Church card">
    <h2 class="church-name"><span class="initial">H</span>arbor <span class="initial">S</span>tone <span class="initial">F</span>ellowship <span class="initial">C</span>hurch</h2>
    <div class="church-contact">
      <p>418 Willow Crest Pkwy suite 3-D Maplecrest GA 30299</p>
      <p>ph. (555)314-8862</p>
      <p class="web">www.Hsfcwebsite.org</p>
    </div>
    <div class="church-illustration" role="img" aria-label="Line illustration of a small church building with a cross"></div>
  </section>

</main>
</body>
</html>
```